Business Card Design Project

I am looking for a classy business card design for a product design consultancy. We specialize in Product Design, Prototyping, and Manufacturing Consulting. Products that we design range from consumer electronics to household products all the way to sporting goods. We are based in Arizona and called "Heron Design Works." We like to have fun and goof off as much as we like to create new products. We are young and energetic so we would like our business cards to reflect that. We already have a logo that we would like to implement into the card design. A plain rectangular business card is boring so feel free to get creative, but please, no avocado shaped cards (it's far too literal). Also feel free to play around with textured card stocks or plastic. The final design that we choose will pay attention to all of the little details. Our cards will need to be 2 sided. We're giving you guys free reign to design as you would like. Please have fun with this, it will reflect in our business card.

Thanks guys,
Heron Design Works Team

Industry/Entity Type

Electronics

Requirements
Must have
• We would like to have a spot UV coating somewhere on the business card design if possible.
Nice to have
• Let's see some designs with custom shapes rather than typical rectangular business cards but please no avocado shaped cards, thanks. Also play around with textured card socks.

```html
<!DOCTYPE html>
<html lang="en">
<head>
<meta charset="utf-8">
<title>Heron Design Works – Business Card</title>
<link rel="stylesheet" href="https://fonts.googleapis.com/css2?family=PT+Sans:wght@400&family=PT+Sans+Narrow&display=swap">
<style>
  :root {
    --leaf: #8dc63f;
    --stone: #8e8e8e;
    --paper: #ffffff;
  }
  * { margin: 0; padding: 0; box-sizing: border-box; }
  html, body {
    width: 993px;
    height: 1200px;
    overflow: hidden;
    background: var(--paper);
    font-family: "PT Sans", sans-serif;
  }
  .sheet { position: relative; width: 993px; height: 1200px; }

  .card {
    position: absolute;
    left: 39px;
    width: 924px;
    border: 1px solid var(--leaf);
    background: var(--paper);
    overflow: hidden;
  }
  .card--front { top: 38px; height: 546px; }
  .card--back  { top: 623px; height: 546px; }

  .brand-name {
    position: absolute;
    font-size: 40px;
    line-height: 1;
    color: var(--stone);
    white-space: nowrap;
  }
  .card--front .brand-name { left: 50%; top: 245px; transform: translateX(-50%); }
  .card--back .brand-name  { left: 77px; top: 122px; }

  .web-band {
    position: absolute;
    left: 0; right: 0;
    top: 456px; height: 32px;
    background: var(--leaf);
    color: var(--paper);
    font-size: 15px;
    letter-spacing: 15px;
    text-align: center;
    line-height: 32px;
    padding-left: 15px;
    white-space: nowrap;
  }

  .side-bar {
    position: absolute;
    left: 0; top: 0; bottom: 0;
    width: 53px;
    background: var(--leaf);
  }
  .person {
    position: absolute;
    right: 183px;
    top: 296px;
    text-align: right;
  }
  .person__name {
    font-variant: small-caps;
    font-size: 38px;
    line-height: 1;
    color: var(--leaf);
    letter-spacing: 0.5px;
  }
  .person__role {
    font-family: "PT Sans Narrow", sans-serif;
    font-size: 28px;
    line-height: 1.1;
    color: var(--stone);
  }
  .divider {
    position: absolute;
    left: 53px;
    top: 377px;
    width: 688px;
    height: 12px;
    background: var(--leaf);
  }
  .contact {
    position: absolute;
    top: 404px;
    list-style: none;
    font-size: 23px;
    line-height: 32.5px;
    color: var(--stone);
    white-space: nowrap;
  }
  .contact--address { left: 77px; }
  .contact--reach { right: 183px; text-align: right; }
</style>
</head>
<body>
<main class="sheet">

  <section class="card card--front" aria-label="Card front">
    <p class="brand-name">Heron Design Works</p>
    <div class="web-band">WWW.HERONDESIGNWORKS.COM</div>
  </section>

  <section class="card card--back" aria-label="Card back">
    <div class="side-bar"></div>
    <p class="brand-name">Heron Design Works</p>
    <div class="person">
      <p class="person__name">First Name Last Name</p>
      <p class="person__role">Designation</p>
    </div>
    <div class="divider"></div>
    <ul class="contact contact--address">
      <li>Address: XYZ Street</li>
      <li>Address Line 2</li>
      <li>Address Line 3</li>
    </ul>
    <ul class="contact contact--reach">
      <li>+0 123 456 7890</li>
      <li>email@herondesignworks.com</li>
      <li>www.herondesignworks.com</li>
    </ul>
  </section>

</main>
</body>
</html>
```